New Property management company business cards

Looking for a new business card, to reflect new younger ownership
Card should be clean, simple and professional but with a modern layout that is conveys our new logo and business model

Key aspects of the business:

Property Management
Facility Maintenance
Project Management
Tenant Improvements

Mailing Address:
PO BOX 7186
Harlow CA, 95471

Phone: 209-614-8837
Direct: 209-614-8831

Doyle Farrant
President

Target Market(s)

Commercial property owners

Industry/Entity Type

Real Estate property management

Contact Information for Business Card

Open to all designs but lean toward vertical layouts

Requirements
Must have
• Logo and space to customize name and contact info

```html
<!DOCTYPE html>
<html lang="en">
<head>
<meta charset="utf-8">
<title>Kestrel Property Management – Business Cards</title>
<link href="https://fonts.googleapis.com/css2?family=Montserrat:wght@500;600&family=Poppins:wght@400;500;600&display=swap" rel="stylesheet">
<style>
  :root {
    --stage: #0a79cc;
    --paper: #f7f7f7;
    --ink: #34323f;
    --teal: #21aca8;
    --white: #ffffff;
  }
  * { margin: 0; padding: 0; box-sizing: border-box; }
  html, body { width: 1200px; height: 1200px; overflow: hidden; }
  body { background: var(--stage); position: relative; font-family: "Poppins", sans-serif; }

  .card {
    position: absolute;
    left: 284px;
    width: 634px;
    height: 362px;
    border-radius: 37px;
    overflow: hidden;
  }
  .card--front { top: 158px; background: var(--paper); }
  .card--back { top: 591px; background: var(--ink); }

  .wordmark {
    position: absolute;
    left: 0; right: 0;
    text-align: center;
    font-family: "Montserrat", sans-serif;
    font-weight: 500;
  }
  .wordmark__name {
    display: block;
    font-size: 38px;
    letter-spacing: 12px;
    line-height: 1;
    padding-left: 12px;
  }
  .wordmark__tag {
    display: block;
    font-size: 12px;
    letter-spacing: 5.6px;
    margin-top: 8px;
    padding-left: 5.6px;
  }
  .card--front .wordmark { top: 172px; color: var(--ink); }
  .card--back .wordmark { top: 121px; color: var(--white); }

  .web-band {
    position: absolute;
    left: 0; right: 0;
    top: 282px;
    height: 33px;
    background: var(--teal);
    color: var(--white);
    font-family: "Montserrat", sans-serif;
    font-weight: 600;
    font-size: 15px;
    letter-spacing: 0.8px;
    text-align: center;
    line-height: 33px;
  }

  .contact-band {
    position: absolute;
    left: 0; right: 0;
    top: 202px;
    height: 120px;
    background: var(--teal);
    color: var(--white);
  }
  .person {
    position: absolute;
    right: 353px;
    top: 34px;
    text-align: right;
  }
  .person__name {
    font-size: 29px;
    line-height: 1;
    font-weight: 400;
    letter-spacing: -0.3px;
  }
  .person__name strong { font-weight: 600; }
  .person__role {
    font-size: 15px;
    font-weight: 500;
    margin-top: 4px;
    letter-spacing: 0.5px;
  }
  .divider {
    position: absolute;
    left: 316px;
    top: 9px;
    width: 1.5px;
    height: 103px;
    background: var(--white);
  }
  .contact-row {
    position: absolute;
    left: 350px;
    display: flex;
    gap: 8px;
    font-size: 12.5px;
    line-height: 14.5px;
    font-weight: 500;
    letter-spacing: 0.8px;
  }
  .contact-row svg { flex: none; margin-top: 1px; }
  .contact-row--address { top: 8px; }
  .contact-row--phone { top: 66px; }
  .contact-row address { font-style: normal; }
</style>
</head>
<body>

  <section class="card card--front">
    <div class="wordmark">
      <span class="wordmark__name">KESTREL</span>
      <span class="wordmark__tag">PROPERTY MANAGEMENT</span>
    </div>
    <div class="web-band">www websiteaddress</div>
  </section>

  <section class="card card--back">
    <div class="wordmark">
      <span class="wordmark__name">KESTREL</span>
      <span class="wordmark__tag">PROPERTY MANAGEMENT</span>
    </div>

    <div class="contact-band">
      <div class="person">
        <p class="person__name"><strong>DOYLE</strong> FARRANT</p>
        <p class="person__role">President</p>
      </div>

      <div class="divider"></div>

      <div class="contact-row contact-row--address">
        <svg width="12" height="16" viewBox="0 0 12 16" aria-hidden="true">
          <path d="M6 0.5a5.5 5.5 0 0 0-5.5 5.5c0 4 5.5 9.5 5.5 9.5s5.5-5.5 5.5-9.5A5.5 5.5 0 0 0 6 0.5z" fill="var(--white)"/>
          <circle cx="6" cy="6" r="2.2" fill="var(--teal)"/>
        </svg>
        <address>PO BOX 7186<br>Harlow CA,<br>95471</address>
      </div>

      <div class="contact-row contact-row--phone">
        <svg width="14" height="15" viewBox="0 0 24 24" aria-hidden="true">
          <path d="M6.6 10.8c1.4 2.8 3.8 5.1 6.6 6.6l2.2-2.2c.3-.3.7-.4 1-.2 1.1.4 2.3.6 3.6.6.6 0 1 .4 1 1V20c0 .6-.4 1-1 1C10.6 21 3 13.4 3 4c0-.6.4-1 1-1h3.5c.6 0 1 .4 1 1 0 1.3.2 2.5.6 3.6.1.3 0 .7-.2 1z" fill="var(--white)"/>
        </svg>
        <p>209-614-8837<br>209-614-8831</p>
      </div>
    </div>
  </section>

</body>
</html>
```